Recipe mobile app, new flow and design for uploading recipe process

I need a new recipe upload process that's simple, intuitive, and engaging.
The goal is to have a user-friendly and fast flow.
The app is a social recipe library where anyone can upload a recipe after signing up. I currently have a flow, but it's "boring," so I'd like to significantly improve this aspect of the app.
When I create a new recipe, it's immediately saved and labeled as a draft. I'll then need to specify:
- Recipe title
- Cover image (required)
- Number of people (how many people is the recipe for)
- Ingredients (name, quantity, and unit of measurement)
- Recipe explanation (broken down into steps, and I can optionally attach an image to each step)
- Upload
Every change is immediately saved, so you can edit, exit, and resume editing later.
I've attached images of the app and the current upload process.
Thank you.
Low design quality
Good morning everyone,
some of the designs received are fantastic, but please make sure to carefully read the requirement so as not to do extra work.
The requirement is to redesign the flow that a user follows when uploading a recipe to the platform.
We have uploaded the current app screens to give you an idea of what the product looks like, what the colors and style are, but we don’t need a full redesign - only the part mentioned above, while keeping the existing style and colors (we cannot rework the entire theme).
To clarify: if you look at the screens shared in the zip file attached to the project, the focus should be on the screens from 5_.png to 10_.png.
These screens can be redesigned in the most creative way you think, as long as the overall theme remains unchanged.
Thank you for your attention.

```html
<!DOCTYPE html>
<html lang="en">
<head>
<meta charset="utf-8">
<title>Recipe Upload Flow</title>
<link href="https://fonts.googleapis.com/css2?family=Montserrat:wght@400;500;600;700;800&display=swap" rel="stylesheet">
<style>
:root{
  --board:#bcbdc1;
  --screen:#ffffff;
  --green:#24a55a;
  --orange:#fb7d3c;
  --ink:#1d1d1f;
  --muted:#5a5a5e;
  --field:#f4f2f3;
  --field-line:#a9a9ad;
  --mint:#e3ede8;
  --card:#f3f1f2;
}
*{box-sizing:border-box;margin:0;padding:0}
html,body{width:1117px;height:1200px;overflow:hidden}
body{background:var(--board);font-family:'Montserrat',sans-serif;color:var(--ink);position:relative}
.screen{position:absolute;width:272px;height:484px;background:var(--screen);overflow:hidden}
.topbar{height:37px;position:relative;box-shadow:0 3px 6px rgba(0,0,0,.06)}
.back{position:absolute;left:12px;top:10px;width:14px;height:18px}
.topbar-title{position:absolute;left:0;right:0;top:12px;text-align:center;font-size:10.5px;font-weight:500}
.next-btn{position:absolute;right:8px;top:8px;height:21px;padding:0 12px;border-radius:11px;background:var(--green);color:#fff;font-size:8.5px;font-weight:800;line-height:21px;letter-spacing:.2px}
.field{position:absolute;left:14px;top:65px;width:245px;height:33px;border:1px solid var(--field-line);border-radius:17px;background:var(--field);font-size:9px;padding-left:20px;line-height:31px}
.field.filled{font-size:11px;color:#333}
.photo-card{position:absolute;left:14px;top:121px;width:245px;height:255px;border-radius:16px;background:var(--card);box-shadow:0 1px 6px rgba(0,0,0,.08);overflow:hidden}
.upload-circle{position:absolute;left:94px;top:22px;width:58px;height:58px;border-radius:50%;background:#fff;box-shadow:0 2px 6px rgba(0,0,0,.08);display:flex;align-items:center;justify-content:center}
.choose-btn{position:absolute;left:76px;top:102px;width:93px;height:25px;border-radius:13px;background:#e0dedf;font-size:10px;text-align:center;line-height:25px}
.kitchen-art{position:absolute;left:0;bottom:0;width:100%;height:106px;background:linear-gradient(90deg,#f6b62e,#f7d37a 30%,#efe6d8 55%,#f6b43a 80%,#e9683a)}
.cover-photo{position:absolute;left:14px;top:122px;width:245px;height:229px;border-radius:18px;background:linear-gradient(135deg,#4a3225 0%,#8b5a3c 35%,#e9dcc6 65%,#cfb48f 100%)}
.question{position:absolute;left:9px;top:58px;font-size:9px;color:#333}
.stepper{position:absolute;left:8px;top:79px;width:258px;height:28px;border:1px solid var(--field-line);border-radius:14px;background:var(--field)}
.stepper .val{position:absolute;left:0;right:0;top:6px;text-align:center;font-size:11px}
.stepper svg{position:absolute;top:7px}
.fab{position:absolute;width:35px;height:35px;border-radius:50%;background:var(--orange);display:flex;align-items:center;justify-content:center}
.ingredient{position:absolute;left:8px;width:257px;height:48px;border-radius:12px;background:var(--mint)}
.ingredient .icon{position:absolute;left:13px;top:9px}
.ingredient .name{position:absolute;left:13px;top:31px;font-size:8px;font-weight:500}
.qty{position:absolute;left:115px;top:7px;width:136px;height:33px;border-radius:10px;background:#fff}
.qty .num{position:absolute;left:12px;top:10px;font-size:10px}
.qty .unit{position:absolute;left:68px;top:0;height:33px;border-left:1px solid #e4e4e4;padding-left:7px;font-size:7px;line-height:33px;width:68px}
.qty .unit svg{position:absolute;right:8px;top:13px}
.step{position:absolute;left:8px;width:255px;height:95px;border-radius:12px;background:var(--mint);overflow:hidden}
.step .shot{position:absolute;left:0;top:0;width:107px;height:95px;border-radius:12px}
.badge{position:absolute;left:132px;top:18px;height:15px;padding:0 8px;border-radius:8px;background:var(--green);color:#fff;font-size:7.5px;font-weight:800;line-height:15px}
.step p{position:absolute;left:132px;top:44px;width:115px;font-size:8.5px;line-height:11.5px;color:#222}
.upload-btn{position:absolute;right:7px;top:9px;height:20px;padding:0 7px;border-radius:10px;background:var(--green);color:#fff;font-size:7.5px;font-weight:800;line-height:20px}
</style>
</head>
<body>

<!-- Screen 1: empty recipe -->
<section class="screen" style="left:90px;top:86px">
  <header class="topbar">
    <svg class="back" viewBox="0 0 14 18"><path d="M10 2 3 9l7 7" fill="none" stroke="#222" stroke-width="1.6"/></svg>
    <span class="next-btn">NEXT</span>
  </header>
  <div class="field">Recipe Name</div>
  <div class="photo-card">
    <div class="upload-circle"><svg width="22" height="22" viewBox="0 0 24 24" fill="none" stroke="#555" stroke-width="1.3"><rect x="3" y="4" width="16" height="16" rx="4"/><circle cx="8" cy="9" r="1.6"/><path d="M3 17l5-4 4 3 3-2 4 3"/><path d="M18 2v6M15.5 4.5 18 2l2.5 2.5"/></svg></div>
    <div class="choose-btn">Choose Photo</div>
    <div class="kitchen-art" role="img" aria-label="Illustration of kitchen bottles, jars, lemons and utensils"></div>
  </div>
</section>

<!-- Screen 2: empty recipe -->
<section class="screen" style="left:403px;top:86px">
  <header class="topbar">
    <svg class="back" viewBox="0 0 14 18"><path d="M10 2 3 9l7 7" fill="none" stroke="#222" stroke-width="1.6"/></svg>
    <span class="next-btn">NEXT</span>
  </header>
  <div class="field">Recipe Name</div>
  <div class="photo-card">
    <div class="upload-circle"><svg width="22" height="22" viewBox="0 0 24 24" fill="none" stroke="#555" stroke-width="1.3"><rect x="3" y="4" width="16" height="16" rx="4"/><circle cx="8" cy="9" r="1.6"/><path d="M3 17l5-4 4 3 3-2 4 3"/><path d="M18 2v6M15.5 4.5 18 2l2.5 2.5"/></svg></div>
    <div class="choose-btn">Choose Photo</div>
    <div class="kitchen-art" role="img" aria-label="Illustration of kitchen bottles, jars, lemons and utensils"></div>
  </div>
</section>

<!-- Screen 3: filled recipe -->
<section class="screen" style="left:715px;top:84px">
  <header class="topbar">
    <svg class="back" viewBox="0 0 14 18"><path d="M10 2 3 9l7 7" fill="none" stroke="#222" stroke-width="1.6"/></svg>
    <span class="next-btn">NEXT</span>
  </header>
  <div class="field filled">Tiramisu</div>
  <div class="cover-photo" role="img" aria-label="Photo of a tiramisu slice dusted with cocoa on a plate"></div>
</section>

<!-- Screen 4: ingredients empty -->
<section class="screen" style="left:90px;top:619px">
  <header class="topbar">
    <svg class="back" viewBox="0 0 14 18"><path d="M10 2 3 9l7 7" fill="none" stroke="#222" stroke-width="1.6"/></svg>
    <span class="topbar-title">Ingredients</span>
    <span class="next-btn">NEXT</span>
  </header>
  <p class="question">For How Many Persons is This Recipe?</p>
  <div class="stepper">
    <svg style="left:8px" width="14" height="14" viewBox="0 0 14 14" fill="none" stroke="#666"><circle cx="7" cy="7" r="6"/><path d="M4 7h6"/></svg>
    <span class="val">4</span>
    <svg style="right:8px" width="14" height="14" viewBox="0 0 14 14" fill="none" stroke="#666"><circle cx="7" cy="7" r="6"/><path d="M4 7h6M7 4v6"/></svg>
  </div>
  <div class="fab" style="left:210px;top:430px"><svg width="14" height="14" stroke="#fff" stroke-width="1.5"><path d="M7 1v12M1 7h12"/></svg></div>
</section>

<!-- Screen 5: ingredients list -->
<section class="screen" style="left:403px;top:619px">
  <header class="topbar">
    <svg class="back" viewBox="0 0 14 18"><path d="M10 2 3 9l7 7" fill="none" stroke="#222" stroke-width="1.6"/></svg>
    <span class="topbar-title">Ingredients</span>
    <span class="next-btn">NEXT</span>
  </header>
  <p class="question">For How Many Persons is This Recipe?</p>
  <div class="stepper">
    <svg style="left:8px" width="14" height="14" viewBox="0 0 14 14" fill="none" stroke="#666"><circle cx="7" cy="7" r="6"/><path d="M4 7h6"/></svg>
    <span class="val">4</span>
    <svg style="right:8px" width="14" height="14" viewBox="0 0 14 14" fill="none" stroke="#666"><circle cx="7" cy="7" r="6"/><path d="M4 7h6M7 4v6"/></svg>
  </div>

  <div class="ingredient" style="top:132px">
    <svg class="icon" width="14" height="16" viewBox="0 0 14 16" fill="none" stroke="var(--green)" stroke-width="1.1"><path d="M5 1h4v3l2 3v8H3V7l2-3z"/></svg>
    <span class="name">MILK</span>
    <div class="qty"><span class="num">250.0</span><span class="unit">Milliliters<svg width="8" height="6"><path d="M1 1l3 3 3-3" fill="none" stroke="#333"/></svg></span></div>
  </div>
  <div class="ingredient" style="top:191px">
    <svg class="icon" width="16" height="16" viewBox="0 0 16 16" fill="none" stroke="var(--green)" stroke-width="1.1"><rect x="3" y="1" width="5" height="4"/><path d="M2 15l3-6h6l3 6z"/></svg>
    <span class="name">SUGAR</span>
    <div class="qty"><span class="num">0.0</span><span class="unit">As Needed<svg width="8" height="6"><path d="M1 1l3 3 3-3" fill="none" stroke="#333"/></svg></span></div>
  </div>
  <div class="ingredient" style="top:250px">
    <svg class="icon" width="16" height="16" viewBox="0 0 16 16" fill="none" stroke="var(--green)" stroke-width="1.1"><rect x="4" y="2" width="8" height="12" transform="rotate(40 8 8)"/><path d="M5 6l6 4M4 9l5 3"/></svg>
    <span class="name">CHOCOLATE</span>
    <div class="qty"><span class="num">10.0</span><span class="unit">Grams<svg width="8" height="6"><path d="M1 1l3 3 3-3" fill="none" stroke="#333"/></svg></span></div>
  </div>
  <div class="ingredient" style="top:309px">
    <svg class="icon" width="18" height="16" viewBox="0 0 18 16" fill="none" stroke="var(--green)" stroke-width="1.1"><ellipse cx="6" cy="9" rx="4" ry="5"/><ellipse cx="12" cy="8" rx="4" ry="5"/></svg>
    <span class="name">EGGS</span>
    <div class="qty"><span class="num">5.0</span><span class="unit">Pieces<svg width="8" height="6"><path d="M1 1l3 3 3-3" fill="none" stroke="#333"/></svg></span></div>
  </div>
  <div class="ingredient" style="top:368px">
    <svg class="icon" width="16" height="16" viewBox="0 0 16 16" fill="none" stroke="var(--green)" stroke-width="1.1"><rect x="5" y="3" width="6" height="12" rx="2" transform="rotate(40 8 9)"/><path d="M11 2l2 2"/></svg>
    <span class="name">WATER</span>
    <div class="qty"><span class="num">500.0</span><span class="unit">Milliliters<svg width="8" height="6"><path d="M1 1l3 3 3-3" fill="none" stroke="#333"/></svg></span></div>
  </div>

  <div class="fab" style="left:210px;top:430px"><svg width="14" height="14" stroke="#fff" stroke-width="1.5"><path d="M7 1v12M1 7h12"/></svg></div>
</section>

<!-- Screen 6: steps -->
<section class="screen" style="left:715px;top:619px">
  <header class="topbar">
    <svg class="back" viewBox="0 0 14 18"><path d="M10 2 3 9l7 7" fill="none" stroke="#222" stroke-width="1.6"/></svg>
    <span class="topbar-title" style="padding-right:0">Steps</span>
    <span class="upload-btn">UPLOAD RECEIPE</span>
  </header>

  <div class="step" style="top:57px">
    <div class="shot" role="img" aria-label="Photo of egg yolks separated in a glass bowl" style="background:linear-gradient(135deg,#8a9a8c,#c7cfc3 50%,#f0a22a 75%,#6d7a70)"></div>
    <span class="badge">STEP 01</span>
    <p>Carefully separate the egg whites, ensuring they are completely free of yolk.</p>
  </div>
  <div class="step" style="top:161px">
    <div class="shot" role="img" aria-label="Photo of beaten egg whites in a glass bowl" style="background:linear-gradient(135deg,#d9d5cf,#f4f2ee 55%,#c9c3bb)"></div>
    <span class="badge">STEP 02</span>
    <p>Beat the egg whites, then add them to the bowl with the mascarpone.</p>
  </div>
  <div class="step" style="top:265px">
    <div class="shot" role="img" aria-label="Photo of a bowl of vanilla cream" style="background:radial-gradient(circle at 50% 50%,#f1e6b8 0 38%,#e5d7a3 45%,#ffffff 50%)"></div>
    <span class="badge">STEP 03</span>
    <p>Sprinkle unsweetened cocoa powder on top.</p>
  </div>
  <div class="step" style="top:369px">
    <div class="shot" role="img" aria-label="Photo of mascarpone cream in a bowl on a dark surface" style="background:radial-gradient(circle at 50% 50%,#f7f5ee 0 34%,#d8d6d0 42%,#2e3234 50%)"></div>
    <span class="badge">STEP 04</span>
    <p>The mascarpone cream is ready.</p>
  </div>

  <div class="fab" style="left:217px;top:438px"><svg width="14" height="14" stroke="#fff" stroke-width="1.5"><path d="M7 1v12M1 7h12"/></svg></div>
</section>

</body>
</html>
```